COBALT YARDS needs bisness cards pronto

Bisness name is "COBALT YARDS" new bisness the bisness includes lawn mowing, garden matanace, and any jobs around the house.
I need a card that is colorful and vibrant and the bisness of lawn mowing maybe with some nature with it. It also needs my contact details"Desmond Larkwell mobile 0412563049 call for free quote and email gwen.brookvale@fernmail.com and a catchy tag line

Requirements
Must have
• Bisness name "COBALT YARDS"
Contact details "0412563049"
Email gwen.brookvale@fernmail.com
Call for free quote

```html
<!DOCTYPE html>
<html lang="en">
<head>
<meta charset="utf-8">
<title>Cobalt Yards – Business Card</title>
<link rel="stylesheet" href="https://fonts.googleapis.com/css2?family=Montserrat:ital,wght@0,600;0,700;1,700&family=Questrial&display=swap">
<style>
  :root {
    --lime: #7ff500;
    --lime-bright: #80ff00;
    --green-dark: #267f00;
    --green-mid: #4fa000;
    --ink: #000000;
    --paper: #ffffff;
    --silhouette: #2b2b2b;
  }
  * { margin: 0; padding: 0; box-sizing: border-box; }
  html, body { width: 1200px; height: 741px; overflow: hidden; background: var(--paper); }
  .card { position: relative; width: 1200px; height: 741px; background: var(--paper); overflow: hidden; }

  .owner-name {
    position: absolute; right: 100px; top: 118px;
    font-family: "Montserrat", sans-serif; font-weight: 700; font-size: 46px;
    color: var(--lime); text-shadow: 3px 4px 4px rgba(0,0,0,0.25);
    white-space: nowrap;
  }
  .owner-name .surname { font-style: italic; }

  .ground-line { position: absolute; left: 0; top: 485px; width: 1200px; height: 2px; background: var(--lime); }

  .mower-scene { position: absolute; left: 0; top: 420px; width: 192px; height: 67px; }

  .brand-name {
    position: absolute; left: 440px; top: 414px;
    font-family: "Questrial", sans-serif; font-weight: 400; font-size: 90px; line-height: 1;
    letter-spacing: 9px;
    color: var(--lime); white-space: nowrap; background: var(--paper); padding: 0 4px 0 8px;
  }

  .tagline {
    position: absolute; right: 100px; top: 512px;
    font-family: "Questrial", sans-serif; font-size: 26px; letter-spacing: 1px;
    color: var(--green-mid); white-space: nowrap;
  }

  .free-quote {
    position: absolute; left: 156px; top: 598px;
    font-family: "Montserrat", sans-serif; font-weight: 600; font-size: 20px;
    letter-spacing: 1px; color: var(--green-dark); white-space: nowrap;
  }

  .contact-band { position: absolute; left: 0; top: 638px; width: 1200px; height: 54px; }
  .swatch { position: absolute; top: 0; height: 50px; }
  .swatch.s1 { left: 0; width: 13px; background: var(--lime-bright); }
  .swatch.s2 { left: 13px; width: 54px; background: var(--green-dark); }
  .swatch.s3 { left: 67px; width: 43px; background: var(--green-mid); }
  .swatch.s4 { left: 110px; width: 14px; background: var(--lime-bright); }
  .swatch-underline { position: absolute; left: 0; top: 50px; width: 124px; height: 4px; background: var(--lime-bright); }

  .phone-block {
    position: absolute; left: 124px; top: 0; width: 411px; height: 50px; background: var(--ink);
    display: flex; align-items: center; padding-left: 32px; gap: 24px;
  }
  .phone-block-underline { position: absolute; left: 124px; top: 50px; width: 411px; height: 4px; background: var(--lime-bright); }
  .phone-icon { width: 44px; height: 44px; flex: none; }
  .phone-number {
    font-family: "Montserrat", sans-serif; font-weight: 600; font-size: 29px;
    letter-spacing: 7px; color: var(--paper);
  }

  .email-block {
    position: absolute; left: 535px; top: 0; width: 665px; height: 50px; background: var(--lime-bright);
    display: flex; align-items: center; padding-left: 44px;
  }
  .email-block-underline { position: absolute; left: 535px; top: 50px; width: 665px; height: 4px; background: var(--ink); }
  .email-address {
    font-family: "Montserrat", sans-serif; font-weight: 700; font-size: 30px; color: var(--paper);
    white-space: nowrap;
  }
</style>
</head>
<body>
<main class="card">
  <h1 class="owner-name">Desmond <span class="surname">Larkwell</span></h1>

  <div class="ground-line"></div>

  <svg class="mower-scene" viewBox="0 0 192 67" role="img" aria-label="Silhouette of a man pushing a lawn mower across a strip of grass">
    <defs>
      <linearGradient id="grass-to-figure" x1="0" x2="1" y1="0" y2="0">
        <stop offset="0" stop-color="#7ff500"/>
        <stop offset="1" stop-color="#2b2b2b"/>
      </linearGradient>
    </defs>
    <rect x="0" y="58" width="192" height="9" fill="#7ff500"/>
    <rect x="108" y="0" width="82" height="67" fill="url(#grass-to-figure)" opacity="0.35"/>
  </svg>

  <div class="brand-name">Cobalt Yards</div>

  <p class="tagline">Sharp cuts, tidy yards, happy homes</p>

  <p class="free-quote">Call for a free quote</p>

  <section class="contact-band">
    <div class="swatch s1"></div>
    <div class="swatch s2"></div>
    <div class="swatch s3"></div>
    <div class="swatch s4"></div>
    <div class="swatch-underline"></div>

    <div class="phone-block">
      <svg class="phone-icon" viewBox="0 0 44 44" aria-hidden="true">
        <circle cx="22" cy="22" r="19" fill="none" stroke="#fff" stroke-width="2.5"/>
        <path d="M26 10 l4 6 -3 2 c-2 3 -3 7 -3 10 l3 1 -2 7 c-5 -1 -7 -8 -5 -15 c1 -5 3 -9 6 -11z" fill="#fff"/>
      </svg>
      <span class="phone-number">0412563049</span>
    </div>
    <div class="phone-block-underline"></div>

    <div class="email-block">
      <span class="email-address">gwen.brookvale@fernmail.com</span>
    </div>
    <div class="email-block-underline"></div>
  </section>
</main>
</body>
</html>
```